Bref créative
business stationary package for dex9firm
envelopes, business cards, 2xcover sheets,ppt template, letterhead, mousepad, cd
Professional
Tobias Wendt
Lindmoosweg 7c
A-1230 Wien
tobias.wendt@dex9firm-example.at
www.dex9firm-example.at
We would need the following templates:
1) letterhead in the size A4
2) ppt presentation in the size A4 landscape
3) business cards in the size of 3.47x2.25in (88,22x57,22mm)
4) single page cover sheet for encrypted emails (A4 portrait)
5) cover sheet for handouts (A4 portrait)
6) mouse pad
7) cd cover sheet+cd design
8) envelope
dex9firm logo
mind: usage without the mirroring effect
demo encrypted message coversheet - ours should look similar but in the dex9firm design - having the same content - we should be able to edit the text
demo for other coversheet - a free rectangle area (cut out) should be placed similar to this upload. We want to print the title on the following page and it should be visible through this cover sheet.

```html
<!DOCTYPE html>
<html lang="en">
<head>
<meta charset="utf-8">
<title>Dex9Firm – Business Cards</title>
<link rel="stylesheet" href="https://fonts.googleapis.com/css2?family=Open+Sans:wght@400;600;700;800&display=swap">
<style>
  :root{
    --bg:#e9e6e1;
    --card-white:#ffffff;
    --brand-blue:#1f5a9c;
    --brand-blue-dark:#123f73;
    --brand-blue-light:#3a7cc4;
    --text-dark:#3b3f45;
    --rule:#c9ced4;
    --on-blue:#ffffff;
  }
  *{margin:0;padding:0;box-sizing:border-box}
  html,body{width:1200px;height:634px;overflow:hidden;background:var(--bg);font-family:"Open Sans",Arial,sans-serif}
  .canvas{position:relative;width:1200px;height:634px}

  .card{position:absolute;box-shadow:0 6px 18px rgba(0,0,0,.25)}

  /* front */
  .card-front{left:67px;top:173px;width:516px;height:331px;background:var(--card-white);overflow:hidden}
  .card-front .wordmark{position:absolute;left:0;right:0;top:46px;text-align:center;font-weight:800;font-size:60px;letter-spacing:-1px;color:var(--brand-blue)}
  .card-front .rule{position:absolute;left:0;right:0;top:150px;height:3px;background:linear-gradient(90deg,transparent,var(--rule) 20%,var(--rule) 80%,transparent)}
  .band{position:absolute;left:0;right:0;top:163px;height:84px;background:linear-gradient(180deg,var(--brand-blue-light),var(--brand-blue) 55%,var(--brand-blue-dark))}
  .band-notch{position:absolute;left:128px;top:-12px}
  .holder-name{position:absolute;left:34px;top:30px;color:var(--on-blue);font-size:17px;font-weight:400}
  .band-divider{position:absolute;left:244px;top:12px;width:1px;height:60px;background:rgba(255,255,255,.6)}
  .contact-list{position:absolute;left:258px;top:14px;list-style:none;color:var(--on-blue);font-size:10.5px;line-height:19px}
  .contact-list li{display:flex;align-items:center;gap:7px;white-space:nowrap}
  .contact-list svg{flex:none}
  .card-front .web{position:absolute;left:0;right:0;top:272px;text-align:center;font-size:17px;font-weight:600;letter-spacing:3px;color:var(--text-dark)}

  /* back */
  .card-back{left:624px;top:156px;width:511px;height:367px;background:radial-gradient(ellipse at 50% 40%,var(--brand-blue-light),var(--brand-blue) 55%,var(--brand-blue-dark))}
  .card-back .wordmark{position:absolute;left:0;right:0;top:124px;text-align:center;font-weight:800;font-size:60px;letter-spacing:-1px;color:var(--on-blue)}
  .card-back .web{position:absolute;left:0;right:0;top:280px;text-align:center;font-size:17px;font-weight:600;letter-spacing:3px;color:var(--on-blue)}
</style>
</head>
<body>
<main class="canvas">
  <section class="card card-front" aria-label="Business card front">
    <div class="wordmark">dex9firm</div>
    <div class="rule"></div>
    <div class="band">
      <svg class="band-notch" width="24" height="12" viewBox="0 0 24 12"><path d="M0 12 L12 0 L24 12 Z" fill="#3a7cc4"/></svg>
      <div class="holder-name">Tobias Wendt</div>
      <div class="band-divider"></div>
      <ul class="contact-list">
        <li><svg width="11" height="11" viewBox="0 0 12 12"><circle cx="6" cy="6" r="6" fill="#fff"/><path d="M6 2.5a2.2 2.2 0 0 0-2.2 2.2C3.8 6.5 6 9.5 6 9.5s2.2-3 2.2-4.8A2.2 2.2 0 0 0 6 2.5z" fill="#1f5a9c"/></svg>Lindmoosweg 7c A-1230 Wien</li>
        <li><svg width="11" height="11" viewBox="0 0 12 12"><circle cx="6" cy="6" r="6" fill="#fff"/><path d="M4 3l1.2 1.6-.6.9a4 4 0 0 0 1.9 1.9l.9-.6L9 8l-.8 1C6 9 3 6 3 3.8z" fill="#1f5a9c"/></svg>+43 660 555 0142</li>
        <li><svg width="11" height="11" viewBox="0 0 12 12"><circle cx="6" cy="6" r="6" fill="#fff"/><rect x="3" y="4" width="6" height="4" fill="none" stroke="#1f5a9c" stroke-width=".9"/><path d="M3 4l3 2.2L9 4" fill="none" stroke="#1f5a9c" stroke-width=".9"/></svg>tobias.wendt@dex9firm-example.at</li>
      </ul>
    </div>
    <div class="web">www.dex9firm-example.at</div>
  </section>

  <section class="card card-back" aria-label="Business card back">
    <div class="wordmark">dex9firm</div>
    <div class="web">www.dex9firm-example.at</div>
  </section>
</main>
</body>
</html>
```